Need a business card design. I am a Self Empowerment Life Coach.

A Life Coach is - a professional relationship designed to enhance an individual's ability to focus, make effective changes, develop oneself, achieve desired goals and maximize success in life. Coaching is about getting the very best out of someone and enabling them to make decisions that will improve their life. It is a unique way to help people look at where they are now and where they would like to be, and helps bridge the gap.

Bright Path Coaching is motivational, inspiring, positive, exciting and action driven. By raising awareness and encouraging others to take responsibility for their life, coaching can help people rise to their challenge and go further than you ever thought possible.

Industry/Entity Type

Business

Other font styles liked:
• Bookman Old Style

Requirements
Must have
• Marla Thorncastle, QTV-AR
• Self Empowerment Coach
• 318.557.6021
• mt@thebloomingpathcoach.example
• The attached logo
Nice to have
• I would like to see some designs portrait and some landscape

```html
<!DOCTYPE html>
<html lang="en">
<head>
<meta charset="utf-8">
<title>Bright Path Coaching – Business Cards</title>
<link rel="stylesheet" href="https://fonts.googleapis.com/css2?family=Oswald:wght@500;700&family=Josefin+Sans:wght@300;400&family=PT+Serif:wght@700&family=Montserrat:wght@700&display=swap">
<style>
  :root {
    --page: #ffffff;
    --card-border: #dcdcdc;
    --navy: #1c3f8c;
    --cyan: #1a8fcf;
    --teal: #0d5f86;
    --ink-soft: #1f6f9a;
    --rule: #6f6f6f;
    --icon: #9a9a9a;
    --wash: #bfe0e9;
    --wash-soft: #e4f1f5;
  }
  * { box-sizing: border-box; margin: 0; padding: 0; }
  html, body {
    width: 1200px; height: 900px; overflow: hidden;
    background: var(--page);
  }
  .sheet { position: relative; width: 1200px; height: 900px; }

  .card {
    position: absolute; top: 104px;
    width: 554px; height: 740px;
    border: 1px solid var(--card-border);
    background: var(--page);
    text-align: center;
  }
  .card--plain { left: 16px; }
  .card--wash {
    left: 601px; top: 102px;
    background: linear-gradient(to bottom,
      #ffffff 0%, var(--wash-soft) 18%, var(--wash) 37%,
      var(--wash-soft) 52%, #ffffff 66%, #ffffff 100%);
  }

  .card > * { position: absolute; left: 0; right: 0; }

  .brand-dot {
    top: 22px; left: 50%; width: 76px; height: 76px; margin-left: -38px;
    right: auto; border-radius: 50%; background: var(--navy);
  }
  .brand-name {
    font-family: "Oswald", sans-serif; font-weight: 700;
    color: var(--navy); text-transform: uppercase; line-height: 1;
  }
  .brand-name--top { top: 112px; font-size: 104px; letter-spacing: -1px; }
  .brand-name--mid { top: 224px; font-size: 104px; letter-spacing: 2px; }
  .brand-name--sub { top: 344px; font-size: 22px; letter-spacing: 12px; padding-left: 12px; }

  .rule {
    left: 50%; right: auto; height: 5px; width: 340px; margin-left: -170px;
    border-radius: 50%;
    background: linear-gradient(to right, transparent, var(--rule) 20%, var(--rule) 80%, transparent);
  }
  .rule--1 { top: 381px; }
  .rule--2 { top: 475px; }
  .rule--3 { top: 585px; }

  .tagline-lead {
    top: 400px; font-family: "Josefin Sans", sans-serif; font-weight: 400;
    font-size: 17px; letter-spacing: 1px; color: var(--navy);
  }
  .tagline-main {
    top: 423px; font-family: "Josefin Sans", sans-serif; font-weight: 300;
    font-size: 44px; letter-spacing: 7px; color: var(--navy);
  }
  .person-name {
    top: 480px; font-family: "Oswald", sans-serif; font-weight: 700;
    font-size: 36px; color: var(--cyan); letter-spacing: 0.5px;
  }
  .person-role {
    top: 547px; font-family: "Josefin Sans", sans-serif; font-weight: 300;
    font-size: 26px; letter-spacing: 1px; color: var(--navy);
  }
  .contact {
    display: flex; justify-content: center; align-items: center; gap: 10px;
  }
  .contact svg { flex: none; }
  .contact--phone {
    top: 600px; font-family: "PT Serif", serif; font-weight: 700;
    font-size: 34px; color: var(--teal);
  }
  .contact--email {
    top: 650px; font-family: "Montserrat", sans-serif; font-weight: 700;
    font-size: 20px; color: var(--ink-soft);
  }
</style>
</head>
<body>
<main class="sheet">

  <section class="card card--plain" aria-label="Business card, white version">
    <div class="brand-dot"></div>
    <div class="brand-name brand-name--top">Bright</div>
    <div class="brand-name brand-name--mid">Path</div>
    <div class="brand-name brand-name--sub">Coaching</div>
    <div class="rule rule--1"></div>
    <p class="tagline-lead">GO FROM SOMEDAY TO</p>
    <p class="tagline-main">TODAY!</p>
    <div class="rule rule--2"></div>
    <h1 class="person-name">MARLA THORNCASTLE, QTV-AR</h1>
    <p class="person-role">SELF EMPOWERMENT COACH</p>
    <div class="rule rule--3"></div>
    <p class="contact contact--phone">
      <svg width="34" height="34" viewBox="0 0 34 34" aria-hidden="true"><circle cx="17" cy="17" r="15.5" fill="none" stroke="var(--icon)" stroke-width="1.5"/><path d="M12 9c1-1 2-1 3 0l2 3c.5 1 0 2-1 2.5-.5.3-.5 1 0 2l2 2.5c.6.7 1.3.8 2 .3 1-.8 2-.8 2.8 0l2 2.2c.8.9.6 2-.5 2.8-3 2-7 0-10.3-4C10 16 9.6 12 12 9z" fill="none" stroke="var(--icon)" stroke-width="1.5"/></svg>
      318.557.6021
    </p>
    <p class="contact contact--email">
      <svg width="34" height="34" viewBox="0 0 34 34" aria-hidden="true"><circle cx="17" cy="17" r="15.5" fill="none" stroke="var(--icon)" stroke-width="1.5"/><rect x="9" y="11.5" width="16" height="11" fill="none" stroke="var(--icon)" stroke-width="1.5"/><path d="M9 11.5l8 6 8-6" fill="none" stroke="var(--icon)" stroke-width="1.5"/></svg>
      mt@thebloomingpathcoach.example
    </p>
  </section>

  <section class="card card--wash" aria-label="Business card, blue wash version">
    <div class="brand-dot"></div>
    <div class="brand-name brand-name--top">Bright</div>
    <div class="brand-name brand-name--mid">Path</div>
    <div class="brand-name brand-name--sub">Coaching</div>
    <div class="rule rule--1"></div>
    <p class="tagline-lead">GO FROM SOMEDAY TO</p>
    <p class="tagline-main">TODAY!</p>
    <div class="rule rule--2"></div>
    <h2 class="person-name">MARLA THORNCASTLE, QTV-AR</h2>
    <p class="person-role">SELF EMPOWERMENT COACH</p>
    <div class="rule rule--3"></div>
    <p class="contact contact--phone">
      <svg width="34" height="34" viewBox="0 0 34 34" aria-hidden="true"><circle cx="17" cy="17" r="15.5" fill="none" stroke="var(--icon)" stroke-width="1.5"/><path d="M12 9c1-1 2-1 3 0l2 3c.5 1 0 2-1 2.5-.5.3-.5 1 0 2l2 2.5c.6.7 1.3.8 2 .3 1-.8 2-.8 2.8 0l2 2.2c.8.9.6 2-.5 2.8-3 2-7 0-10.3-4C10 16 9.6 12 12 9z" fill="none" stroke="var(--icon)" stroke-width="1.5"/></svg>
      318.557.6021
    </p>
    <p class="contact contact--email">
      <svg width="34" height="34" viewBox="0 0 34 34" aria-hidden="true"><circle cx="17" cy="17" r="15.5" fill="none" stroke="var(--icon)" stroke-width="1.5"/><rect x="9" y="11.5" width="16" height="11" fill="none" stroke="var(--icon)" stroke-width="1.5"/><path d="M9 11.5l8 6 8-6" fill="none" stroke="var(--icon)" stroke-width="1.5"/></svg>
      mt@thebloomingpathcoach.example
    </p>
  </section>

</main>
</body>
</html>
```